we are an outdoor outlet in a country club that has a variety of outlets. The Club is called Brookhaven and is located in Cairo, Egypt. This garden menu will include cuisines from the Mediterranean, Asia and Texmex. we need a menu that is colorful and would fit an A3 size, back and front are to be used. Attached is the old menu currently in use (Garden Menu 2012.pdf is just for reference) and the new menu text for you to use is under the name Garden Menu Fall 2013
thank you.

```html
<!DOCTYPE html>
<html lang="en">
<head>
<meta charset="utf-8">
<title>Brookhaven Garden Menu – Fall 2013</title>
<link href="https://fonts.googleapis.com/css2?family=Parisienne&family=Satisfy&family=Raleway:wght@400;600&display=swap" rel="stylesheet">
<style>
  :root{
    --backdrop:#efece6;
    --paper:#ffffff;
    --sand:#e2ddd4;
    --mist:#f1efeb;
    --magenta:#b8325a;
    --lime:#c5d35c;
    --lime-soft:#dfe79f;
    --teal:#3b8ea6;
    --olive:#8f9a2c;
    --cocoa:#5b2b2b;
    --stone:#8d8781;
    --ink:#4a4440;
  }
  *{box-sizing:border-box;margin:0;padding:0}
  html,body{width:1200px;height:800px;overflow:hidden}
  body{background:var(--backdrop);font-family:"Raleway",sans-serif;color:var(--ink);position:relative}

  .sheet{position:absolute;top:30px;width:540px;height:740px;background:var(--paper);box-shadow:0 2px 10px rgba(0,0,0,.12);overflow:hidden}
  .sheet--mediterranean{left:30px}
  .sheet--asian-texmex{left:630px}

  .band{position:absolute;left:0;width:100%}
  .divider{position:absolute;left:20px;right:20px;height:10px}

  .corner-title{font-family:"Parisienne",cursive;font-size:30px;color:var(--cocoa);line-height:1}
  .section-title{font-family:"Parisienne",cursive;font-size:21px;line-height:1;margin:8px 0 4px}
  .section-title--lime{color:var(--olive)}
  .section-title--teal{color:var(--teal)}
  .section-title--magenta{color:var(--magenta)}

  .menu-list{list-style:none}
  .menu-item{margin-bottom:5px}
  .menu-item__name{font-family:"Satisfy",cursive;font-size:14px;color:var(--cocoa);display:flex;justify-content:space-between}
  .menu-item__price{font-family:"Raleway",sans-serif;font-size:8px;color:var(--stone);align-self:center}
  .menu-item__desc{font-size:8px;color:var(--stone);letter-spacing:.2px}

  .column{position:absolute}

  .art{position:absolute}

  /* Mediterranean sheet */
  .med-top{top:0;height:300px}
  .med-middle{top:310px;height:240px}
  .med-cover{top:560px;height:180px;background:var(--sand)}

  .appetizer-box{position:absolute;left:230px;top:8px;width:290px;height:222px;background:var(--lime-soft);padding:12px 16px}
  .appetizer-box .menu-item__name{font-size:13px}
  .appetizer-box .menu-item{display:flex;align-items:center;gap:6px;margin-bottom:7px}
  .bullet{width:5px;height:5px;border-radius:50%;background:var(--magenta);flex:none}

  .cover-title{position:absolute;left:24px;top:108px;font-family:"Parisienne",cursive;font-size:32px;color:var(--magenta);line-height:1}
  .cover-brand{position:absolute;left:30px;top:30px;display:flex;align-items:center;gap:8px}
  .brand-name{font-family:"Raleway",sans-serif;font-weight:600;font-size:20px;color:var(--stone);letter-spacing:1px}
  .brand-dot{width:12px;height:12px;border-radius:50%;background:var(--lime)}

  .toppings{font-size:8px;color:var(--stone)}

  /* Asian / Tex-Mex sheet */
  .tex-top{top:0;height:300px}
  .asian-middle{top:310px;height:250px;background:var(--mist)}
  .tex-salads{top:570px;height:170px}

  .sheet-brand{position:absolute;right:20px;top:14px;display:flex;align-items:center;gap:6px}
  .sheet-brand .brand-name{font-size:12px}
  .sheet-brand .brand-dot{width:8px;height:8px}
</style>
</head>
<body>

<!-- Mediterranean sheet -->
<section class="sheet sheet--mediterranean" aria-label="Garden menu, Mediterranean side">

  <div class="band med-top">
    <div class="column" style="left:24px;top:12px;width:220px">
      <h3 class="section-title section-title--lime">Salads</h3>
      <ul class="menu-list">
        <li class="menu-item"><p class="menu-item__name">Caprese <span class="menu-item__price">EGP 48</span></p><p class="menu-item__desc">Tomato, mozzarella, basil, olive oil</p></li>
        <li class="menu-item"><p class="menu-item__name">Greek Salad <span class="menu-item__price">EGP 42</span></p><p class="menu-item__desc">Feta, olives, cucumber, oregano</p></li>
        <li class="menu-item"><p class="menu-item__name">Fattoush <span class="menu-item__price">EGP 38</span></p><p class="menu-item__desc">Crisp pita, sumac, fresh greens</p></li>
      </ul>
      <h3 class="section-title section-title--teal">Sandwiches</h3>
      <ul class="menu-list">
        <li class="menu-item"><p class="menu-item__name">Chicken Shawarma <span class="menu-item__price">EGP 45</span></p><p class="menu-item__desc">Garlic sauce, pickles, fries</p></li>
        <li class="menu-item"><p class="menu-item__name">Falafel Wrap <span class="menu-item__price">EGP 32</span></p><p class="menu-item__desc">Tahini, tomato, fresh herbs</p></li>
      </ul>
    </div>
    <div class="column" style="left:280px;top:12px;width:236px">
      <h3 class="section-title section-title--teal">Pizza &amp; Pasta</h3>
      <ul class="menu-list">
        <li class="menu-item"><p class="menu-item__name">Margherita <span class="menu-item__price">EGP 55</span></p><p class="menu-item__desc">Tomato sauce, mozzarella, basil</p></li>
        <li class="menu-item"><p class="menu-item__name">Penne Arrabbiata <span class="menu-item__price">EGP 50</span></p><p class="menu-item__desc">Spicy tomato, garlic, parsley</p></li>
      </ul>
      <h3 class="section-title section-title--magenta">Toppings</h3>
      <p class="toppings">Mushroom, olives, pepperoni, extra cheese</p>
      <h3 class="section-title section-title--magenta">Main Courses</h3>
      <ul class="menu-list">
        <li class="menu-item"><p class="menu-item__name">Grilled Kofta <span class="menu-item__price">EGP 75</span></p><p class="menu-item__desc">Rice, grilled vegetables, tahini</p></li>
        <li class="menu-item"><p class="menu-item__name">Shish Tawook <span class="menu-item__price">EGP 70</span></p><p class="menu-item__desc">Marinated chicken, garlic dip</p></li>
      </ul>
    </div>
  </div>

  <svg class="divider" style="top:300px" viewBox="0 0 500 10" preserveAspectRatio="none" aria-hidden="true">
    <line x1="0" y1="5" x2="500" y2="5" stroke="#b8325a" stroke-width="1"/>
    <circle cx="250" cy="5" r="3" fill="#b8325a"/>
  </svg>

  <div class="band med-middle">
    <div class="column" style="left:24px;top:10px;width:195px">
      <h2 class="corner-title">Mediterranean Corner</h2>
      <h3 class="section-title section-title--magenta">Soups</h3>
      <ul class="menu-list">
        <li class="menu-item"><p class="menu-item__name">Tomato Basil <span class="menu-item__price">EGP 28</span></p><p class="menu-item__desc">Roasted tomato, cream, basil</p></li>
        <li class="menu-item"><p class="menu-item__name">Chicken Cream <span class="menu-item__price">EGP 30</span></p><p class="menu-item__desc">Chicken, mushroom, light cream</p></li>
        <li class="menu-item"><p class="menu-item__name">Moroccan Harira <span class="menu-item__price">EGP 30</span></p><p class="menu-item__desc">Lentils, chickpeas, warm spices</p></li>
      </ul>
    </div>
    <div class="appetizer-box">
      <h3 class="section-title section-title--magenta" style="margin-top:0">Appetizers</h3>
      <ul class="menu-list">
        <li class="menu-item"><span class="bullet"></span><p class="menu-item__name">Hummus with toasted pine nuts</p></li>
        <li class="menu-item"><span class="bullet"></span><p class="menu-item__name">Baba ghanoush with pomegranate</p></li>
        <li class="menu-item"><span class="bullet"></span><p class="menu-item__name">Stuffed vine leaves with lemon</p></li>
        <li class="menu-item"><span class="bullet"></span><p class="menu-item__name">Fried kibbeh with yogurt dip</p></li>
        <li class="menu-item"><span class="bullet"></span><p class="menu-item__name">Labneh with mint and olive oil</p></li>
        <li class="menu-item"><span class="bullet"></span><p class="menu-item__name">Grilled halloumi with thyme</p></li>
      </ul>
    </div>
  </div>

  <div class="band med-cover">
    <div class="art" role="img" aria-label="Illustration of stylised garden flowers and leaves in magenta, lime and grey" style="left:190px;top:0;width:350px;height:180px;background:linear-gradient(120deg,#cfc9bf 0%,#c9d46a 45%,#b8325a 100%);opacity:.85"></div>
    <div class="cover-brand"><span class="brand-dot"></span><span class="brand-name">Brookhaven</span></div>
    <h1 class="cover-title">Garden Menu<br>Fall 2013</h1>
  </div>
</section>

<!-- Asian & Tex-Mex sheet -->
<section class="sheet sheet--asian-texmex" aria-label="Garden menu, Asian and Tex-Mex side">

  <div class="band tex-top">
    <div class="sheet-brand"><span class="brand-dot"></span><span class="brand-name">Brookhaven</span></div>
    <div class="column" style="left:24px;top:12px;width:250px">
      <h2 class="corner-title">Tex Mex</h2>
      <h3 class="section-title section-title--lime">Appetizers</h3>
      <ul class="menu-list">
        <li class="menu-item"><p class="menu-item__name">Nachos <span class="menu-item__price">EGP 40</span></p><p class="menu-item__desc">Cheese, jalapeño, salsa</p></li>
        <li class="menu-item"><p class="menu-item__name">Buffalo Wings <span class="menu-item__price">EGP 48</span></p><p class="menu-item__desc">Blue cheese dip</p></li>
      </ul>
      <h3 class="section-title section-title--magenta">Main Courses &amp; Sandwiches</h3>
      <ul class="menu-list">
        <li class="menu-item"><p class="menu-item__name">Quesadillas <span class="menu-item__price">EGP 55</span></p><p class="menu-item__desc">Chicken, peppers, sour cream</p></li>
        <li class="menu-item"><p class="menu-item__name">Fajita Chicken Wrap <span class="menu-item__price">EGP 52</span></p><p class="menu-item__desc">Guacamole, salsa, cheddar</p></li>
        <li class="menu-item"><p class="menu-item__name">Chili con Carne <span class="menu-item__price">EGP 60</span></p><p class="menu-item__desc">Beans, rice, tortilla chips</p></li>
      </ul>
    </div>
    <div class="column" style="left:290px;top:40px;width:120px">
      <h3 class="section-title section-title--magenta">Desserts</h3>
      <ul class="menu-list">
        <li class="menu-item"><p class="menu-item__name">Churros</p><p class="menu-item__desc">Cinnamon sugar, chocolate dip</p></li>
        <li class="menu-item"><p class="menu-item__name">Brownie Sundae</p><p class="menu-item__desc">Vanilla ice cream</p></li>
        <li class="menu-item"><p class="menu-item__name">Tres Leches</p><p class="menu-item__desc">Three milk sponge</p></li>
      </ul>
    </div>
    <div class="art" role="img" aria-label="Illustration of patterned cacti with a magenta flower" style="left:420px;top:60px;width:110px;height:230px;background:linear-gradient(180deg,#dfe79f 0%,#c5d35c 60%,#b8325a 100%);border-radius:40px 40px 0 0"></div>
  </div>

  <svg class="divider" style="top:300px" viewBox="0 0 500 10" preserveAspectRatio="none" aria-hidden="true">
    <line x1="0" y1="5" x2="500" y2="5" stroke="#8d8781" stroke-width="1"/>
    <circle cx="250" cy="5" r="3" fill="#b8325a"/>
  </svg>

  <div class="band asian-middle">
    <div class="art" role="img" aria-label="Illustration of large leaves and a magenta blossom with bamboo shadows" style="left:0;top:0;width:150px;height:250px;background:linear-gradient(160deg,#dcd8cf 0%,#c5d35c 55%,#b8325a 100%);opacity:.8"></div>
    <div class="column" style="left:165px;top:10px;width:170px">
      <h2 class="corner-title">Asian Corner</h2>
      <h3 class="section-title section-title--lime">Salads &amp; Appetizers</h3>
      <ul class="menu-list">
        <li class="menu-item"><p class="menu-item__name">Chicken Wasabi Salad</p><p class="menu-item__desc">Greens, wasabi dressing, sesame</p></li>
        <li class="menu-item"><p class="menu-item__name">Chicken Sesame Noodle Salad</p><p class="menu-item__desc">Noodles, peanut, soy dressing</p></li>
        <li class="menu-item"><p class="menu-item__name">Spring Rolls</p><p class="menu-item__desc">Vegetables, sweet chili sauce</p></li>
        <li class="menu-item"><p class="menu-item__name">Indian Samosa</p><p class="menu-item__desc">Potato, peas, mint chutney</p></li>
      </ul>
    </div>
    <div class="column" style="left:350px;top:44px;width:170px">
      <h3 class="section-title section-title--magenta">Main Courses</h3>
      <ul class="menu-list">
        <li class="menu-item"><p class="menu-item__name">Mango Chicken Mallai</p><p class="menu-item__desc">Creamy mango, basmati rice</p></li>
        <li class="menu-item"><p class="menu-item__name">Chicken Tandoori</p><p class="menu-item__desc">Yogurt spices, naan bread</p></li>
        <li class="menu-item"><p class="menu-item__name">Thai Coconut Curry Shrimp</p><p class="menu-item__desc">Coconut milk, jasmine rice</p></li>
        <li class="menu-item"><p class="menu-item__name">Mongolian Beef</p><p class="menu-item__desc">Scallions, soy glaze, rice</p></li>
      </ul>
    </div>
  </div>

  <div class="band tex-salads">
    <div class="column" style="left:24px;top:10px;width:300px">
      <h2 class="corner-title">Tex Mex</h2>
      <h3 class="section-title section-title--teal">Salads</h3>
      <ul class="menu-list" style="display:flex;gap:30px">
        <li class="menu-item"><p class="menu-item__name">Caesar Salad</p><p class="menu-item__desc">Romaine, croutons, parmesan dressing</p></li>
        <li class="menu-item"><p class="menu-item__name">Taco Salad</p><p class="menu-item__desc">Crispy shell, beef, beans</p></li>
      </ul>
    </div>
    <div class="art" role="img" aria-label="Faint illustration of bamboo stems and leaves" style="left:340px;top:10px;width:180px;height:150px;background:linear-gradient(180deg,#f1efeb 0%,#dcd8cf 100%)"></div>
  </div>
</section>

</body>
</html>
```